Spectral Geology services flyer

We are looking for some eye-catching flyer designs templates for our company spectral geology pages. We are open to any designs but prefer the theme colour to be similar to our logo colours or something goes well with the colours.
We have attached a pptx that has texts and figures we would like to put on the flyer, please combined slide 1&2 as front page and 3-5 as back page.
Requirements:
Colour theme: similar to logo colours or something that goes well with it (logo is attached)
Page: two sides A4 size
Text & front: No specific requirements
Reference/examples:
- Below website demonstrates how we use our machines for those applications
http://www.brinvaleoptics.com/applications_home.html
- Same applies to slide 11 - 25 from link below
http://www.norrikwade.com.au/public/documents/5/18/Crustal%20Survey%20of%20Ancient%20Copper%20Belts.pdf

```html
<!DOCTYPE html>
<html lang="en">
<head>
<meta charset="utf-8">
<title>Spectral Geology and Earth Imagery</title>
<link rel="stylesheet" href="https://fonts.googleapis.com/css2?family=Bebas+Neue&family=Pathway+Gothic+One&display=swap">
<style>
  :root {
    --backdrop: #d3d3d3;
    --brand-blue: #0b6ea8;
    --text-blue: #1766a6;
    --paper: #ffffff;
    --sand: #f8d6b4;
    --orange: #ef9a5a;
    --deep-orange: #e36f2a;
  }
  html, body {
    margin: 0;
    width: 1200px;
    height: 1200px;
    overflow: hidden;
    background: var(--backdrop);
  }
  .flyer {
    position: absolute;
    left: 176px;
    top: 0;
    width: 848px;
    height: 1200px;
    overflow: hidden;
    background: linear-gradient(to bottom, var(--paper) 0%, var(--paper) 18%, #fdf3ea 40%, var(--sand) 62%, var(--orange) 82%, var(--deep-orange) 100%);
    font-family: "Pathway Gothic One", "Arial Narrow", sans-serif;
    color: var(--text-blue);
  }
  .field-photo {
    position: absolute;
    left: 0;
    top: 820px;
    width: 848px;
    height: 380px;
    background: linear-gradient(to bottom, rgba(239,154,90,0) 0%, rgba(232,130,70,0.55) 35%, rgba(227,111,42,0.85) 100%);
  }
  .title-band {
    position: absolute;
    left: 0;
    top: 60px;
    width: 848px;
    height: 64px;
    background: var(--brand-blue);
    color: var(--paper);
    font-family: "Bebas Neue", "Arial Narrow", sans-serif;
    font-size: 46px;
    line-height: 64px;
    text-align: center;
    letter-spacing: 0.5px;
  }
  .notch { position: absolute; left: 0; top: 123px; }
  .rule {
    position: absolute;
    width: 3px;
    background: var(--brand-blue);
  }
  .rule-right { left: 803px; top: 158px; height: 632px; }
  .rule-left { left: 43px; top: 218px; height: 702px; }
  .copy {
    position: absolute;
    font-size: 25px;
    line-height: 34.4px;
    white-space: nowrap;
  }
  .copy-left { left: 66px; text-align: left; }
  .copy-right { right: 66px; text-align: right; }
  .cta-peak { position: absolute; left: 758px; top: 949px; }
  .cta-band {
    position: absolute;
    left: 0;
    top: 998px;
    width: 848px;
    height: 142px;
    background: var(--brand-blue);
    color: var(--paper);
    text-align: center;
    font-size: 25px;
    line-height: 34.4px;
    padding-top: 21px;
    box-sizing: border-box;
  }
</style>
</head>
<body>
  <main class="flyer">
    <div class="field-photo" role="img" aria-label="Photo of geologists in hard hats surveying a field site, tinted orange"></div>

    <h1 class="title-band" style="margin:0;font-weight:400;">SPECTRAL GEOLOGY AND EARTH IMAGERY</h1>
    <svg class="notch" width="90" height="48" viewBox="0 0 90 48"><polygon points="0,0 88,0 40,47" fill="#0b6ea8"/></svg>

    <div class="rule rule-right"></div>
    <div class="rule rule-left"></div>

    <p class="copy copy-right" style="top:153px;margin:0;">Terranova Ore Insights provides a complete SPECTRAL GEOLOGY TRAINING service</p>

    <p class="copy copy-left" style="top:213px;margin:0;">Courses on equipment use, licencing and data interpretation are available to early<br>career geoscientists, senior geologists and exploration managers across<br>Asia, Africa, Australia, Canada, Europe, Pacific Rim Nations and South America</p>

    <p class="copy copy-right" style="top:343px;margin:0;">Learn how PSM / KSX specialists acquire and validate spectral data from<br>soil, rock chip and downhole samples (chips and core)</p>

    <p class="copy copy-left" style="top:437px;margin:0;">Understand how Spectral Geologist’s interpret PSM / KSX strip logs, develop<br>alteration models and identify mineralisation vectors</p>

    <p class="copy copy-right" style="top:533px;margin:0;">Meet senior geologists that integrate spectral data with drilling, false-colour<br>imagery (satellite data), lithology, geochemical assays, geochronology, geophysics,<br>radiometrics and structure to generate high-quality exploration targets</p>

    <p class="copy copy-left" style="top:662px;margin:0;">Participate in a case-study where generative consultants integrate alteration<br>models and mineralisation vectors with field mapping, mineral distribution<br>intensity and abundance maps, grade shell models, geophysics and tectonic<br>models to produce new exploration concepts</p>

    <p class="copy copy-right" style="top:825px;margin:0;">See how marketing and promotions specialists incorporate PSM data into high<br>impact graphics for public release and to communicate investment<br>opportunities to market participants and senior management</p>

    <svg class="cta-peak" width="90" height="50" viewBox="0 0 90 50"><polygon points="0,50 48,0 90,44 90,50" fill="#0b6ea8"/></svg>
    <section class="cta-band">
      TRAINED TEAMS MAKE BREAKTHROUGHS<br>
      Ask our Competent Persons and QAQC experts how to report PSM results<br>
      in accordance with JORC and NI43-101 standards
    </section>
  </main>
</body>
</html>
```